Law Firm Website

I currently have a temporary site that I created myself at www.mcorveyfirm.net (hosted by 9tree). I am generally happy with the content.

My permanent website just has basic information right now: www.mcorveyfirm.com (hosted by lumenrack). I want to take the general content from the temporary website and have a more professional looking website on the permanent website. I want it in Wordpress format. I want a link to my blog: www.crookedpath.com. I want it to work on pads and smart phones. My number and e-mail address should be available on every page. The idea is to feature the potential client more than the lawyer.
Updates

Several of the designs are good. I would like the front page to have my number and address at the top (and at the top of every page) and to identify my law firm as "Law Office of Gerald T. Corvey". No need to include "mcorveyfirm" as that is just the web address. I like showing the most recent blog posts on the front page. I don't need video. No need to emphasize office hours or map location on the front page (that could be under a contact button). My picture should be somewhere. I would like an image from Boston on the front page if we can find one that is not copyright protected. No images of gavels or scales of justice. See some of the sample websites I listed in previous messages. Thanks!

Industry/Entity Type

Law Firm

```html
<!DOCTYPE html>
<html lang="en">
<head>
<meta charset="utf-8">
<title>Law Office of Gerald T. Corvey</title>
<link href="https://fonts.googleapis.com/css2?family=Ubuntu:wght@300;400;500;700&display=swap" rel="stylesheet">
<style>
:root{
  --ink:#2b2b2b;
  --muted:#555;
  --blue:#4aa3dd;
  --blue-dark:#3a8ccb;
  --band:#e8e9eb;
  --rule:#8a8a8a;
  --footer:#4d4d4d;
  --white:#fff;
  --accent-red:#c0392b;
}
*{box-sizing:border-box;margin:0;padding:0}
html,body{width:912px;height:1200px;overflow:hidden;background:var(--white)}
body{position:relative;font-family:"Ubuntu",sans-serif;color:var(--ink)}
.abs{position:absolute}
a{color:inherit}

.site-title{left:54px;top:21px;font-size:24px;font-weight:500;color:var(--ink)}
.contact-line{left:439px;top:15px;font-size:11px;color:var(--ink);display:flex;align-items:center;gap:5px;white-space:nowrap}
.contact-line svg{flex:none}
.phone{right:56px;top:36px;font-size:22px;font-weight:700;color:var(--blue);display:flex;align-items:center;gap:6px}

.main-nav{left:54px;top:77px;width:804px;display:flex;justify-content:space-between;font-size:11px;color:var(--ink)}

.hero-band{left:0;top:126px;width:912px;height:228px;background:var(--band)}
.hero-photo{left:50px;top:107px;width:365px;height:221px;background:linear-gradient(120deg,#1c1c1c 0%,#3a3f46 45%,#6f8aa6 75%,#c9d8e6 100%)}
.hero-panel{left:415px;top:107px;width:220px;height:221px;background:linear-gradient(160deg,#2a5b86,#173a5c);color:var(--white);padding:37px 0 0 19px}
.hero-panel p{font-size:14.5px;line-height:20px;font-weight:300}
.btn{display:inline-block;background:var(--blue);color:var(--white);font-size:10px;font-weight:500;padding:5px 11px;text-decoration:none}
.hero-panel .btn{margin-top:13px}
.service-menu{left:635px;top:100px;width:228px;height:236px;background:var(--white);box-shadow:0 1px 3px rgba(0,0,0,.25)}
.service-menu .item{position:absolute;left:18px;font-size:10px;font-weight:500;color:var(--ink)}
.service-menu .active{left:0;top:0;width:228px;height:59px;background:linear-gradient(#fff,#ececec);padding:24px 0 0 18px}
.service-menu .sep{position:absolute;left:18px;width:190px;height:1px;background:var(--rule)}
.menu-arrow{left:612px;top:100px}

.intro-title{font-size:23px;font-weight:300;color:#444}
.intro-title b{font-weight:500}
.intro-left{left:53px;top:384px;width:340px}
.portrait{left:56px;top:419px;width:82px;height:102px;background:linear-gradient(#6a6f78,#2d333d)}
.intro-text{left:152px;top:419px;width:244px;font-size:10.4px;line-height:13px;font-weight:300;color:var(--muted);letter-spacing:.35px}
.intro-text a{color:var(--accent-red);display:block;margin-top:3px}
.divider{left:421px;top:372px;width:1px;height:160px;background:var(--rule)}
.intro-right{left:445px;top:384px;width:418px}
.intro-right p{margin-top:9px;font-size:10.4px;line-height:13px;font-weight:300;color:var(--muted);letter-spacing:.35px}
.intro-right .btn{margin-top:10px}

.areas-band{left:0;top:550px;width:912px;height:283px;background:linear-gradient(180deg,#c9cacc 0%,#8f9194 45%,#4d5054 70%,#b3b5b8 100%)}
.areas-title{left:315px;top:591px;width:282px;height:33px;background:var(--white);text-align:center;font-size:21px;font-weight:500;color:var(--blue);line-height:33px}
.area-card{top:644px;width:113px;height:150px;background:var(--white);box-shadow:0 1px 3px rgba(0,0,0,.3)}
.area-card .icon{height:107px;background:var(--blue);display:flex;align-items:center;justify-content:center}
.area-card .icon svg{width:76px;height:66px;fill:none;stroke:var(--white);stroke-width:1.8;stroke-linejoin:round;stroke-linecap:round}
.area-card .label{height:43px;display:flex;align-items:center;justify-content:center;text-align:center;font-size:8.5px;line-height:10px;color:var(--ink);padding:0 8px}

.col-title{font-size:23px;font-weight:300;color:var(--blue);line-height:26px}
.follow{left:47px;top:853px;width:200px}
.small{font-size:9.5px;line-height:12px;color:var(--muted);font-weight:300;letter-spacing:.2px}
.socials{left:45px;top:941px;display:flex;gap:8px;align-items:center}
.social{display:flex;align-items:center;gap:4px;font-size:9.5px;color:var(--ink)}
.social i{width:26px;height:26px;background:var(--blue-dark);display:block}
.subscribe{left:47px;top:993px;width:190px}
.subscribe .btn{margin-top:8px;font-size:12px;padding:7px 21px}

.posts{left:266px;top:853px;width:310px}
.posts ul{list-style:none;margin-top:9px}
.posts li{font-size:9.5px;line-height:12px;color:var(--muted);font-weight:300;letter-spacing:.35px;padding:8px 0 8px;border-bottom:1px dashed var(--rule)}
.posts li:first-child{padding-top:2px}
.posts li:last-child{border-bottom:0}
.posts li a{text-decoration:underline}

.request{left:623px;top:853px;width:238px}
.field{border:1px solid #bbb;height:26px;font-size:9.5px;color:var(--muted);padding:7px 7px;margin-bottom:10px}
.field.area{height:76px}
.request form{margin-top:10px}
.request .btn{font-size:11px;padding:8px 29px;margin-top:-1px}

.footer{left:0;top:1128px;width:912px;height:72px;background:var(--footer);color:#eee;text-align:center;font-size:10px;font-weight:300;padding-top:21px;line-height:16px}
</style>
</head>
<body>

<header>
  <div class="abs site-title">Law Office of Gerald T. Corvey</div>
  <div class="abs contact-line">58 Harbor Row 3rd Floor Boston, MA 02110
    <svg width="10" height="14" viewBox="0 0 10 14"><path d="M5 0a5 5 0 0 0-5 5c0 4 5 9 5 9s5-5 5-9a5 5 0 0 0-5-5z" fill="#444"/><circle cx="5" cy="5" r="2" fill="#fff"/></svg>
    <span style="margin-left:4px">gcorvey@mcorveyfirm.com</span>
    <svg width="17" height="12" viewBox="0 0 17 12"><rect width="17" height="12" rx="1" fill="#444"/><path d="M1 1l7.5 6L16 1" stroke="#fff" stroke-width="1.3" fill="none"/></svg>
  </div>
  <div class="abs phone">(617) 555-0142
    <svg width="18" height="14" viewBox="0 0 18 14"><path d="M1 5c0-3 16-3 16 0l-1 2h-3l-1-2H6L5 7H2z" fill="#444"/><rect x="4" y="7" width="10" height="6" rx="1" fill="#444"/><circle cx="9" cy="10" r="1.6" fill="#fff"/></svg>
  </div>
  <nav class="abs main-nav">
    <span>Home</span><span>Why Hire Me?</span><span>Success Stories</span><span>Practice Areas</span><span>Representative Clients</span><span>Services Provided</span><span>Contact Us</span><span>How to Find Us</span>
  </nav>
</header>

<section class="hero">
  <div class="abs hero-band"></div>
  <div class="abs hero-photo" role="img" aria-label="Photo of a lawyer in a dark suit and blue tie in an office"></div>
  <div class="abs hero-panel">
    <p>Hiring and Firing.<br>Wage and Hour Issues.<br>Noncompetes.<br>Sexual Harassment.<br>Leave Issues under the<br>ADA, FMLA and State Law.</p>
    <a class="btn" href="#">Read more</a>
  </div>
  <svg class="abs menu-arrow" width="24" height="59" viewBox="0 0 24 59"><path d="M24 0v59L0 29.5z" fill="#f4f4f4"/></svg>
  <div class="abs service-menu">
    <div class="item active">Employment Counseling &amp; Litigation</div>
    <div class="item" style="top:83px">Business Litigation</div>
    <div class="sep" style="top:115px"></div>
    <div class="item" style="top:139px">Litigation Avoidance</div>
    <div class="sep" style="top:175px"></div>
    <div class="item" style="top:198px">Businesss partner/shareholder Disputes</div>
  </div>
</section>

<section class="intro">
  <h2 class="abs intro-left intro-title">Law Office of <b>Gerald T. Corvey</b></h2>
  <div class="abs portrait" role="img" aria-label="Portrait photo of attorney Gerald T. Corvey"></div>
  <p class="abs intro-text">I have over fifteen years of experience handling business and employment litigation and counseling for private businesses and for owners and professionals. I serve as de facto outside general counsel to several private Massachusetts businesses. I have successfully handled a number of jury and jury-waived trials.<a href="#">Read more</a></p>
  <div class="abs divider"></div>
  <div class="abs intro-right">
    <h2 class="intro-title">Practical Advice</h2>
    <p>I give real, practical advice to keep you out of trouble, stay in business and make money. I won't bore you with legal theories, but will explain how the legal issues affect your business. I have a passion for helping businesses and other clients. If you are sued or have to sue another business, customer or ex-employee or business partner, I will develop the right, cost effective strategy with you.</p>
    <a class="btn" href="#">Read more</a>
  </div>
</section>

<section class="practice-areas">
  <div class="abs areas-band" role="img" aria-label="Black and white photo of the Boston skyline along the waterfront"></div>
  <h2 class="abs areas-title">PRACTICE AREAS</h2>

  <div class="abs area-card" style="left:81px">
    <div class="icon"><svg viewBox="0 0 76 66" aria-hidden="true">
      <path d="M4 22l12-12 8 8-12 12z"/><path d="M72 22L60 10l-8 8 12 12z"/>
      <path d="M22 16l10-4 8 2 8-2 8 6"/>
      <path d="M12 30l22 22c2 2 5 2 7 0"/><path d="M64 30L44 50"/>
      <path d="M30 24l8 8M26 36l8 8M32 32l8 8M38 28l8 8"/>
      <path d="M40 14L30 24c-2 2 0 5 3 4l9-7"/>
    </svg></div>
    <div class="label">BUSINESS AND CORPORATE LAW</div>
  </div>

  <div class="abs area-card" style="left:229px">
    <div class="icon"><svg viewBox="0 0 76 66" aria-hidden="true">
      <path d="M52 62V8l16-6v60"/><path d="M56 14h8M56 20h8M56 26h8M56 32h8M56 38h8"/>
      <path d="M2 62h72"/>
      <path d="M6 62V44l12-10 12 10v18"/><path d="M26 62V40l12-10 14 12v20"/>
      <path d="M10 50h5v5h-5zM32 46h5v5h-5zM42 46h5v5h-5zM36 56v6h6v-6z"/>
    </svg></div>
    <div class="label">REAL ESTATE LAW</div>
  </div>

  <div class="abs area-card" style="left:377px">
    <div class="icon"><svg viewBox="0 0 76 66" aria-hidden="true">
      <path d="M18 4h40v44L44 62H18z"/><path d="M44 62V48h14"/>
      <circle cx="38" cy="18" r="6"/><path d="M34 23l-2 8 6-3 6 3-2-8"/>
      <path d="M26 38h24M26 43h16"/>
    </svg></div>
    <div class="label">PROBATE LAW</div>
  </div>

  <div class="abs area-card" style="left:525px">
    <div class="icon"><svg viewBox="0 0 76 66" aria-hidden="true">
      <circle cx="28" cy="9" r="6"/><circle cx="48" cy="13" r="5"/><circle cx="38" cy="32" r="4"/>
      <path d="M18 62V22h20v10"/><path d="M22 62V44M34 40v22"/>
      <path d="M42 30V22h14v30h-4v10"/>
      <path d="M32 62V42h12v20M38 48v14"/>
    </svg></div>
    <div class="label">ESTATE PLANNING</div>
  </div>

  <div class="abs area-card" style="left:674px">
    <div class="icon"><svg viewBox="0 0 76 66" aria-hidden="true">
      <path d="M30 12V6h16v6"/>
      <path d="M8 16l48-4 12 8v34l-48 6-12-10z"/><path d="M20 24v36M8 16l12 8 48-4"/>
      <path d="M38 30h8v-8h8v8h8v8h-8v8h-8v-8h-8z"/>
    </svg></div>
    <div class="label">SERIOUS PERSONAL INJURY LAW</div>
  </div>
</section>

<section class="lower">
  <div class="abs follow">
    <h3 class="col-title">Follow<br>Gerald T. Corvey</h3>
    <p class="small" style="margin-top:6px">Follow us for the latest world of work insights and news.</p>
  </div>
  <div class="abs socials">
    <span class="social"><i></i>Friendlink</span>
    <span class="social"><i></i>Chirply</span>
    <span class="social"><i></i>Workweb</span>
  </div>
  <div class="abs subscribe">
    <h3 class="col-title">Subscribe</h3>
    <p class="small" style="margin-top:3px">Receive email alerts from<br>Gerald T. Corvey and get our latest<br>press releases, financial news and<br>research products.</p>
    <a class="btn" href="#">Subscribe</a>
  </div>

  <div class="abs posts">
    <h3 class="col-title">Latest Posts</h3>
    <ul>
      <li><a href="#">You're Damned If You Don't Respond Appropriately to a Poor Rateline Review or Online Post</a></li>
      <li><a href="#">You're Damned if You Don't Settle Meritorious Discrimination Cases</a></li>
      <li><a href="#">You May Be Damned if Your Drunk Employee Leaves the Company Party and Kills Someone in a Car Accident.</a></li>
      <li><a href="#">Reflecting on Owning A Business</a></li>
      <li><a href="#">You Are Damned if You Annoy Your Customers</a></li>
      <li><a href="#">You're Damned if You Don't Fire Your Favorite Employees</a></li>
      <li><a href="#">You're Damned If You Are Sexually Obsessed With an Employee</a></li>
    </ul>
  </div>

  <div class="abs request">
    <h3 class="col-title">Request call</h3>
    <form>
      <div class="field">Name</div>
      <div class="field">Email</div>
      <div class="field">Contact No.</div>
      <div class="field area">Your Query</div>
      <a class="btn" href="#">SUBMIT</a>
    </form>
  </div>
</section>

<footer class="abs footer">
  Home | Why Hire Me? | Success Stories | Practice Areas | Representative Clients | Services Provided | Contact Us<br>
  Copyright © 2010 Law Office of Gerald T. Corvey. All rights reserved.
</footer>

</body>
</html>
```